Business card for a "family office" company

Please provide professional looking business card designs, incorporating the attached logo and below details. Harrowmere Holdings Pty Ltd is a family office / financial investment company. We are looking for a modern, professional and contemporary card design.

Industry/Entity Type

Finance

Contact Information for Business Card

Name: Dean Mollick
Title: Director
Company: Harrowmere Holdings Pty Ltd
Email: harrowdean@quillnet.example
Mobile: 0462 735 418
Address: 4/312 Barnaby Parade, Brackenmoor WA 6218, Australia

Requirements
Must have
• All details above and the logo. logo only on back side. incorporate colours of logo
Nice to have
• up to you
Should not have
• ?

```html
<!DOCTYPE html>
<html lang="en">
<head>
<meta charset="utf-8">
<title>Harrowmere Holdings – Business Card</title>
<link href="https://fonts.googleapis.com/css2?family=Roboto:wght@400;500&display=swap" rel="stylesheet">
<style>
  :root {
    --navy: #1f1e5a;
    --royal: #2b3896;
    --royal-edge: #3a4bb0;
    --paper: #ffffff;
    --ink: #1f1e5a;
    --backdrop: #6a7276;
    --text-light: #ffffff;
  }
  * { box-sizing: border-box; margin: 0; padding: 0; }
  html, body {
    width: 1200px; height: 900px; overflow: hidden;
    background: var(--backdrop);
    font-family: "Roboto", Arial, sans-serif;
  }
  .sheet {
    width: 1200px; height: 900px;
    display: flex; flex-direction: column;
    align-items: center; justify-content: center; gap: 44px;
  }
  .card {
    position: relative;
    width: 620px; height: 379px;
    overflow: hidden;
    box-shadow: 0 10px 28px rgba(0,0,0,.35);
  }
  .card-shapes { position: absolute; inset: 0; }

  /* front */
  .card-front { background: var(--paper); }
  .front-brand {
    position: absolute; left: 46px; top: 58px;
    display: flex; align-items: center; gap: 12px;
    color: var(--ink);
  }
  .brand-mark { width: 22px; height: 22px; background: currentColor; flex: none; }
  .brand-name {
    font-weight: 500; font-size: 23px; letter-spacing: 3px;
    line-height: 1.15; text-transform: uppercase;
  }
  .contact-list {
    position: absolute; left: 46px; top: 206px;
    list-style: none; color: var(--ink);
    font-size: 15px; display: flex; flex-direction: column; gap: 12px;
  }
  .contact-item { display: flex; align-items: center; gap: 10px; }
  .contact-icon { width: 20px; height: 20px; flex: none; }
  .name-tab {
    position: absolute; right: 0; top: 48px;
    width: 230px; height: 74px;
    padding: 14px 26px 0 0;
    text-align: right; color: var(--text-light);
  }
  .person-name { font-size: 24px; font-weight: 400; }
  .person-title { font-size: 12px; margin-top: 4px; }
  .address {
    position: absolute; right: 28px; bottom: 34px;
    text-align: right; color: var(--text-light);
    font-size: 15px; line-height: 1.45;
  }

  /* back */
  .card-back {
    background: var(--navy);
    display: flex; align-items: center; justify-content: center;
  }
  .back-brand {
    display: flex; align-items: center; gap: 16px;
    color: var(--text-light);
  }
  .back-brand .brand-mark { width: 30px; height: 30px; }
  .back-brand .brand-name { font-size: 32px; letter-spacing: 4px; }
</style>
</head>
<body>
<main class="sheet">

  <section class="card card-front" aria-label="Business card front">
    <svg class="card-shapes" viewBox="0 0 620 379" aria-hidden="true">
      <polygon points="420,0 620,0 620,379 270,379" fill="var(--navy)"/>
      <polygon points="412,48 620,48 620,122 390,122 400,70" fill="var(--royal)"/>
      <polygon points="400,70 412,48 430,48 418,70" fill="var(--royal-edge)"/>
    </svg>

    <div class="front-brand">
      <span class="brand-mark"></span>
      <span class="brand-name">Harrowmere<br>Holdings</span>
    </div>

    <ul class="contact-list">
      <li class="contact-item">
        <svg class="contact-icon" viewBox="0 0 20 20" aria-hidden="true">
          <rect width="20" height="20" fill="var(--ink)"/>
          <path d="M6 4.5l2 0 1 3-1.5 1a7 7 0 0 0 4 4l1-1.5 3 1 0 2a1.5 1.5 0 0 1-1.5 1.5A10 10 0 0 1 4.5 6 1.5 1.5 0 0 1 6 4.5z" fill="#fff"/>
        </svg>
        <span>0462 735 418</span>
      </li>
      <li class="contact-item">
        <svg class="contact-icon" viewBox="0 0 20 20" aria-hidden="true">
          <rect width="20" height="20" fill="var(--ink)"/>
          <rect x="4" y="6" width="12" height="8" fill="none" stroke="#fff" stroke-width="1.4"/>
          <path d="M4 6l6 5 6-5" fill="none" stroke="#fff" stroke-width="1.4"/>
        </svg>
        <span>harrowdean@quillnet.example</span>
      </li>
    </ul>

    <div class="name-tab">
      <p class="person-name">Dean Mollick</p>
      <p class="person-title">Director</p>
    </div>

    <p class="address">4/312 Barnaby Parade<br>Brackenmoor WA 6218, Australia</p>
  </section>

  <section class="card card-back" aria-label="Business card back">
    <div class="back-brand">
      <span class="brand-mark"></span>
      <span class="brand-name">Harrowmere Holdings</span>
    </div>
  </section>

</main>
</body>
</html>
```